Kestrel Works Business Cards

This job is for the design of a business card.
I would like to review the design in 2x colour tones to choose from black and white inverted.
EG:
Black with white logo and white with black logo on BACK
White with black text on front and black with white text options
PRINTING DIMENSIONS: 4.5 x 8.5cm
Complete design will need to be provided in ready to print format with bleed lines
Target Market(s)
The audience of my business are people in the trade industry.
It will be also used for general networking with trades people and possible future clients.
I want to be represented as a professional, dynamic, creative and personable operator.
The card should reflect style, taste, experience, professionalism.
Industry/Entity Type
Business
Requirements
Must have
- BACK CONTENT:
- Logo in white and black background and vice versa with WHITE card and black logo review samples.
- FRONT CARD CONTENT:
- Name: Morgan Telvane
- Director
- Phone: 0438 216 947
- Email: morgan@kestrelworks.com.au
- Web: kestrelworks.com.au
- LICENCE #: KT-R 72158
Nice to have
- Possibly a textured background design on rear as a pose to a solid black
- Possibly adding a blue or orange discreet colour tone (possibly for email, phone abbreviated letter or symbols).

```html
<!DOCTYPE html>
<html lang="en">
<head>
<meta charset="utf-8">
<title>Kestrel Works – Business Cards</title>
<link rel="stylesheet" href="https://fonts.googleapis.com/css2?family=Roboto+Condensed:wght@400;700&display=swap">
<style>
  :root {
    --page: #e9e7e3;
    --card-white: #ffffff;
    --card-white-edge: #ececec;
    --card-black: #0c0c0c;
    --card-black-glow: #2e2e2e;
    --ink: #111111;
    --ink-soft: #333333;
    --paper-ink: #ffffff;
    --rule: #1a1a1a;
  }
  * { box-sizing: border-box; margin: 0; padding: 0; }
  html, body {
    width: 1200px; height: 1024px; overflow: hidden;
    background: var(--page);
    font-family: "Roboto Condensed", "Arial Narrow", sans-serif;
  }
  .sheet {
    width: 1200px; height: 1024px;
    display: flex; flex-direction: column; align-items: center; justify-content: center;
    gap: 44px;
  }
  .card {
    width: 850px; height: 450px;
    position: relative;
    overflow: hidden;
    box-shadow: 0 10px 28px rgba(0,0,0,.22);
  }

  /* Front */
  .card--front {
    background: linear-gradient(135deg, var(--card-white) 55%, var(--card-white-edge));
    color: var(--ink);
  }
  .front__brand {
    position: absolute; left: 110px; top: 100px;
    font-weight: 700; font-size: 54px; letter-spacing: 2px; line-height: 1;
    text-transform: uppercase; color: var(--ink);
  }
  .front__divider {
    position: absolute; left: 0; right: 0; top: 206px;
    display: flex; align-items: flex-end;
  }
  .front__rule {
    height: 2px; background: var(--rule);
    margin-bottom: 5px;
  }
  .front__rule--lead { flex: 1; }
  .front__rule--tail { width: 48px; }
  .front__name {
    font-size: 27px; line-height: 1; letter-spacing: 1px;
    text-transform: uppercase; white-space: nowrap;
    margin: 0 14px 0 16px;
  }
  .front__role {
    position: absolute; right: 62px; top: 242px;
    font-size: 22px; line-height: 1; color: var(--ink-soft);
  }
  .front__contacts {
    position: absolute; left: 110px; top: 290px;
    list-style: none; display: flex; flex-direction: column; gap: 8px;
    font-size: 21px; font-weight: 700; line-height: 25px;
  }
  .front__contacts li { display: flex; align-items: center; gap: 22px; }
  .front__contacts svg { width: 20px; height: 20px; flex: none; }

  /* Back */
  .card--back {
    background: radial-gradient(ellipse at 50% 48%, var(--card-black-glow) 0%, var(--card-black) 70%);
    color: var(--paper-ink);
    display: flex; align-items: center; justify-content: center;
  }
  .back__brand {
    font-weight: 700; font-size: 86px; letter-spacing: 4px;
    text-transform: uppercase; color: var(--paper-ink);
  }
</style>
</head>
<body>
<main class="sheet">
  <section class="card card--front" aria-label="Card front">
    <div class="front__brand">Kestrel Works</div>
    <div class="front__divider">
      <span class="front__rule front__rule--lead"></span>
      <span class="front__name">Morgan Telvane</span>
      <span class="front__rule front__rule--tail"></span>
    </div>
    <div class="front__role">Director</div>
    <ul class="front__contacts">
      <li>
        <svg viewBox="0 0 20 20" aria-hidden="true"><rect x="5" y="1.5" width="10" height="17" rx="2" fill="none" stroke="#111" stroke-width="2"/><circle cx="10" cy="15.3" r="1.2" fill="#111"/></svg>
        <span>0438 216 947</span>
      </li>
      <li>
        <svg viewBox="0 0 20 20" aria-hidden="true"><rect x="1.5" y="4" width="17" height="12" rx="1.5" fill="#111"/><path d="M2.5 5 10 11l7.5-6" fill="none" stroke="#fff" stroke-width="1.6"/></svg>
        <span>morgan@kestrelworks.com.au</span>
      </li>
      <li>
        <svg viewBox="0 0 20 20" aria-hidden="true"><circle cx="10" cy="10" r="8.3" fill="none" stroke="#111" stroke-width="1.8"/><ellipse cx="10" cy="10" rx="3.6" ry="8.3" fill="none" stroke="#111" stroke-width="1.4"/><path d="M2 10h16M3.5 6h13M3.5 14h13" stroke="#111" stroke-width="1.3"/></svg>
        <span>www.kestrelworks.com.au</span>
      </li>
      <li>
        <svg viewBox="0 0 20 20" aria-hidden="true"><rect x="3.5" y="1.5" width="13" height="17" rx="1.5" fill="none" stroke="#111" stroke-width="1.8"/><path d="M6.5 6.5h7M6.5 10h7M6.5 13.5h4" stroke="#111" stroke-width="1.5"/></svg>
        <span>Licence # KT-R 72158</span>
      </li>
    </ul>
  </section>

  <section class="card card--back" aria-label="Card back">
    <div class="back__brand">Kestrel Works</div>
  </section>
</main>
</body>
</html>
```